Plumvale CEO needs a Crowdsourced Graphic for a Wirelark Article

I need a simple graphic / banner for a blog post that's going to be posted on Wirelark (www.wirelark.com) - the biggest tech blog in the world.

The article will be written by Tobin Marsh (Plumvale's CEO) and the title will be "Asia's Secret Crowdsourcing Boom". The article is about the tens of thousands of people using crowdsourcing websites (like Plumvale.com, Qorvel.com and Vantrio.com) in China, India, the Philippines, Australia and other countries in the Asia Pacific region.

We'd really like to get this ASAP - so early submissions encouraged. We will try and get the winning designer linked to from the article.

Thanks to everyone that submitted!  Some great designs and hard to choose! :)

Target Market(s)

Tech saavy readers, English speakers

Industry/Entity Type

Tech

Requirements
Must have
• The graphic SHOULD:
1) Have the text "Asia's secret crowdsourcing boom" with some nice design and fonts (consider grey subtle pattern background and white drop shadow on fonts) - see attached examples
2) Have an Asian theme
3) Have the dimensions 640px wide by 240px wide
Nice to have
• The graphic COULD:
1) Have references to some or all of the countries mentioned above or use Asian characters as part of the background / motif (maybe the word "crowd" or "crowd sourcing" in different languages). In Chinese, the word for crowdsourcing is "witkey" (and there are corresponding Chinese characters: ??)
2) Emphasize the word "Asia" (using color and larger/different font)
3) Use a chart showing exponential (i.e. fast) growth - like the attached
4) Have a second line of text "5 Things You Didn't Know About Crowdsourcing in Asia"

```html
<!DOCTYPE html>
<html lang="en">
<head>
<meta charset="utf-8">
<title>Asia's Secret Crowdsourcing Boom</title>
<link href="https://fonts.googleapis.com/css2?family=Bowlby+One&family=Montserrat:ital,wght@1,900&family=Roboto+Condensed:wght@500;700&display=swap" rel="stylesheet">
<style>
  :root {
    --bg-light: #c9c9c7;
    --bg-mid: #a9a9a7;
    --bg-dark: #8e8e8c;
    --map-green: #3fae2a;
    --map-green-soft: #7fcf55;
    --asia-gold: #f2c200;
    --asia-gold-light: #ffe34d;
    --outline: #2b2410;
    --band: #f4f4f2;
    --ink: #111111;
    --subtitle: #3a3420;
    --bar-green: #5cc21a;
    --bar-light: #b8ee48;
    --bar-edge: #e8f060;
  }
  html, body {
    margin: 0;
    padding: 0;
    overflow: hidden;
    background: #ffffff;
  }
  .banner {
    position: relative;
    width: 1200px;
    height: 450px;
    overflow: hidden;
    background:
      radial-gradient(ellipse at 55% 45%, var(--bg-light) 0%, var(--bg-mid) 60%, var(--bg-dark) 100%);
  }
  .asia-map {
    position: absolute;
    left: 0;
    top: 0;
    width: 390px;
    height: 320px;
    background: radial-gradient(ellipse at 40% 40%, var(--map-green-soft) 0%, var(--map-green) 45%, rgba(63,174,42,0) 72%);
    opacity: 0.9;
  }
  .title-asia {
    position: absolute;
    left: 535px;
    top: 2px;
    margin: 0;
    font-family: "Bowlby One", sans-serif;
    font-size: 92px;
    line-height: 1;
    letter-spacing: 2px;
    color: var(--asia-gold);
    background: linear-gradient(180deg, var(--asia-gold-light) 0%, var(--asia-gold) 60%, #d9a400 100%);
    -webkit-background-clip: text;
    background-clip: text;
    -webkit-text-fill-color: transparent;
    -webkit-text-stroke: 3px var(--outline);
    filter: drop-shadow(3px 3px 0 rgba(255,255,255,0.7));
  }
  .title-band {
    position: absolute;
    left: 118px;
    top: 112px;
    width: 620px;
    height: 80px;
  }
  .title-line {
    position: absolute;
    left: 140px;
    top: 120px;
    margin: 0;
    display: flex;
    align-items: baseline;
    gap: 10px;
    color: var(--ink);
    line-height: 1;
    text-transform: uppercase;
    text-shadow: 2px 2px 0 rgba(255,255,255,0.8);
  }
  .title-secret {
    font-family: "Montserrat", sans-serif;
    font-style: italic;
    font-weight: 900;
    font-size: 50px;
  }
  .title-crowdsourcing {
    font-family: "Roboto Condensed", sans-serif;
    font-weight: 500;
    font-size: 50px;
  }
  .title-boom {
    font-family: "Montserrat", sans-serif;
    font-weight: 900;
    font-size: 50px;
    font-style: normal;
  }
  .subtitle {
    position: absolute;
    left: 28px;
    top: 292px;
    margin: 0;
    font-family: "Roboto Condensed", sans-serif;
    font-weight: 700;
    font-size: 40px;
    line-height: 46px;
    letter-spacing: 0.5px;
    text-transform: uppercase;
    color: var(--subtitle);
    text-shadow: 1px 1px 0 rgba(255,255,255,0.5);
  }
  .growth-chart {
    position: absolute;
    left: 0;
    top: 0;
    width: 1200px;
    height: 450px;
  }
</style>
</head>
<body>
  <div class="banner">
    <div class="asia-map" role="img" aria-label="Green map of Asia and the Pacific region"></div>

    <svg class="title-band" viewBox="0 0 620 80" aria-hidden="true">
      <defs>
        <linearGradient id="band-fade" x1="0" x2="1" y1="0" y2="0">
          <stop offset="0" stop-color="#f4f4f2" stop-opacity="0"/>
          <stop offset="0.08" stop-color="#f4f4f2" stop-opacity="0.95"/>
          <stop offset="0.92" stop-color="#f4f4f2" stop-opacity="0.95"/>
          <stop offset="1" stop-color="#f4f4f2" stop-opacity="0"/>
        </linearGradient>
      </defs>
      <rect x="0" y="0" width="620" height="80" fill="url(#band-fade)"/>
    </svg>

    <h1 class="title-asia">Asia's</h1>
    <p class="title-line">
      <span class="title-secret">Secret</span>
      <span class="title-crowdsourcing">Crowdsourcing</span>
      <span class="title-boom">Boom</span>
    </p>

    <p class="subtitle">5 Things You Didn't Know<br>About Crowdsourcing in Asia</p>

    <svg class="growth-chart" viewBox="0 0 1200 450" aria-label="Bar chart showing fast growth" role="img">
      <defs>
        <linearGradient id="bar-fill" x1="0" x2="1" y1="0" y2="0">
          <stop offset="0" stop-color="#3d9a10"/>
          <stop offset="0.5" stop-color="#b8ee48"/>
          <stop offset="1" stop-color="#5cc21a"/>
        </linearGradient>
        <linearGradient id="arrow-fill" x1="0" x2="1" y1="1" y2="0">
          <stop offset="0" stop-color="#5cc21a" stop-opacity="0"/>
          <stop offset="0.35" stop-color="#4fb81a"/>
          <stop offset="1" stop-color="#2f9a0c"/>
        </linearGradient>
      </defs>

      <g class="chart-bars" stroke="#e8f060" stroke-width="2.5">
        <rect x="850" y="345" width="32" height="77" fill="url(#bar-fill)"/>
        <rect x="893" y="335" width="32" height="87" fill="url(#bar-fill)"/>
        <rect x="936" y="310" width="32" height="112" fill="url(#bar-fill)"/>
        <rect x="984" y="262" width="32" height="160" fill="url(#bar-fill)"/>
        <rect x="1040" y="188" width="34" height="234" fill="url(#bar-fill)"/>
        <rect x="1104" y="140" width="36" height="282" fill="url(#bar-fill)"/>
      </g>

      <g class="growth-arrow">
        <path d="M640 410 C 820 380, 980 320, 1100 95 L 1118 103 C 1000 335, 830 395, 640 410 Z" fill="url(#arrow-fill)"/>
        <polygon points="1080,100 1160,22 1146,132" fill="#2f9a0c"/>
      </g>
    </svg>
  </div>
</body>
</html>
```